Sonstige Design für Bild mit Produktvorteilen
Zielgruppe
Herstellung und Vertrieb von Kinderspieltürmen für den Garten.
Aufgabenstellung
Wir suchen ein Bild was Produktvorteile darstellt. Das Bild soll als zusätzlichen Produktbild in unserem Shop / Kaufro / Velmora verwendet werden.
Vorteile:
- 10 Jahre Garantie
- Extra dicke Pofosten 9 x 9 cm
- Premium Holz glatt gehobelt
- Kesseldruckimprägniert, kein streichen notwendig
Beispielpordukt: https://www.kranzlober.net/green-otter-spielturm-sand-cove-mit-rutsche-2-30-m-rampe-mit-seil

```html
<!DOCTYPE html>
<html lang="de">
<head>
<meta charset="utf-8">
<title>Produktvorteile Spielturm</title>
<link rel="stylesheet" href="https://fonts.googleapis.com/css2?family=Raleway:wght@500&family=Montserrat:wght@700&display=swap">
<style>
  :root {
    --sky-top: #c9dcec;
    --sky-bottom: #e4edf4;
    --grass-top: #5f8a2c;
    --grass-bottom: #2f5414;
    --photo-light: #d8cba6;
    --photo-dark: #a8a07a;
    --text-dark: #262626;
    --accent-orange: #f39200;
    --tick-green: #5aa82a;
  }
  * { margin: 0; padding: 0; box-sizing: border-box; }
  html, body { width: 1200px; height: 740px; overflow: hidden; }
  body { position: relative; background: var(--sky-bottom); }

  .sky {
    position: absolute; left: 0; top: 0; width: 1200px; height: 496px;
    background: linear-gradient(180deg, var(--sky-top) 0%, var(--sky-bottom) 70%, #f2f6f9 100%);
  }
  .lawn {
    position: absolute; left: 0; top: 496px; width: 1200px; height: 244px;
    background: linear-gradient(180deg, var(--grass-top) 0%, var(--grass-bottom) 100%);
  }
  .product-photo {
    position: absolute; left: 74px; top: 60px; width: 380px; height: 612px;
    background: linear-gradient(180deg, var(--photo-light) 0%, var(--photo-dark) 100%);
    opacity: 0.85;
  }

  .benefits {
    position: absolute; left: 548px; top: 67px; list-style: none;
  }
  .benefit {
    position: relative; padding-left: 56px; margin-bottom: 17px;
  }
  .benefit:first-child { margin-bottom: 18px; }
  .benefit .tick {
    position: absolute; left: 0; top: 28px; width: 44px; height: 40px;
  }
  .benefit:first-child .tick { top: 5px; }
  .benefit-title {
    display: block;
    font-family: "Raleway", sans-serif; font-weight: 500;
    font-size: 43px; line-height: 50px; color: var(--text-dark);
    letter-spacing: 0.3px;
  }
  .benefit-note {
    display: block;
    font-family: "Montserrat", sans-serif; font-weight: 700;
    font-size: 25px; line-height: 36px; color: var(--accent-orange);
  }
</style>
</head>
<body>
  <div class="sky" role="img" aria-label="Hellblauer Himmel mit Wolken"></div>
  <div class="lawn" role="img" aria-label="Grüne Rasenfläche"></div>
  <div class="product-photo" role="img" aria-label="Produktfoto: Holz-Spielturm mit Dach, Leiter, Sandkasten und grüner Rutsche, auf dem Kinder spielen"></div>

  <ul class="benefits">
    <li class="benefit">
      <svg class="tick" viewBox="0 0 44 40" aria-hidden="true"><path d="M3 22 L16 34 L41 4" fill="none" stroke="var(--tick-green)" stroke-width="8" stroke-linecap="round" stroke-linejoin="round"/></svg>
      <span class="benefit-title">10 Jahre Garantie</span>
    </li>
    <li class="benefit">
      <svg class="tick" viewBox="0 0 44 40" aria-hidden="true"><path d="M3 22 L16 34 L41 4" fill="none" stroke="var(--tick-green)" stroke-width="8" stroke-linecap="round" stroke-linejoin="round"/></svg>
      <span class="benefit-title">Extra dicke Pfosten</span>
      <span class="benefit-note">9x9 cm</span>
    </li>
    <li class="benefit">
      <svg class="tick" viewBox="0 0 44 40" aria-hidden="true"><path d="M3 22 L16 34 L41 4" fill="none" stroke="var(--tick-green)" stroke-width="8" stroke-linecap="round" stroke-linejoin="round"/></svg>
      <span class="benefit-title">Premium Holz</span>
      <span class="benefit-note">glatt gehobelt</span>
    </li>
    <li class="benefit">
      <svg class="tick" viewBox="0 0 44 40" aria-hidden="true"><path d="M3 22 L16 34 L41 4" fill="none" stroke="var(--tick-green)" stroke-width="8" stroke-linecap="round" stroke-linejoin="round"/></svg>
      <span class="benefit-title">Kesseldruckimprägniert</span>
      <span class="benefit-note">kein Streichen notwendig</span>
    </li>
  </ul>
</body>
</html>
```